Business Card Design Project

We're an orthopaedic office, and our colors are blue white and balck. Dealing with physicians and healthcare execs, I'd like this card to have a classy, yet overpowering wow factor.

Here are a couple of cards I like that are close to what I'm looking for:
http://www.plumvantia.com/design/671583
http://www.plumvantia.com/design/514515

```html
<!DOCTYPE html>
<html lang="en">
<head>
<meta charset="utf-8">
<title>Crestline Orthopaedic – Business Card</title>
<link rel="stylesheet" href="https://fonts.googleapis.com/css2?family=Source+Sans+3:wght@400;600&display=swap">
<style>
  :root {
    --backdrop: #2b2b2b;
    --card-navy: #0c2b5f;
    --card-navy-deep: #0a2553;
    --ink-white: #ffffff;
    --ink-soft: #e4eaf4;
  }
  * { margin: 0; padding: 0; box-sizing: border-box; }
  html, body {
    width: 1200px; height: 900px; overflow: hidden;
    background: var(--backdrop);
    font-family: "Source Sans 3", "Myriad Pro", Arial, sans-serif;
    color: var(--ink-white);
  }
  .canvas { position: relative; width: 1200px; height: 900px; }
  .card {
    position: absolute; top: 308px;
    width: 513px; height: 284px;
    background: var(--card-navy);
    overflow: hidden;
    box-shadow: 0 3px 8px rgba(0,0,0,0.45);
  }
  .card--front { left: 73px; }
  .card--back { left: 616px; }

  .brand-mark { position: absolute; background: var(--ink-white); }
  .brand { position: absolute; display: flex; flex-direction: column; align-items: flex-end; line-height: 1; }
  .brand__name { font-weight: 400; letter-spacing: 0.3px; white-space: nowrap; }
  .brand__tagline { font-weight: 400; text-align: right; line-height: 1.1; white-space: nowrap; }

  .card--front .brand-mark { left: 113px; top: 86px; width: 104px; height: 104px; }
  .card--front .brand { left: 230px; top: 128px; }
  .card--front .brand__name { font-size: 35px; }
  .card--front .brand__tagline { font-size: 13.5px; margin-top: 2px; }

  .card--back .brand-mark { left: 27px; top: 32px; width: 86px; height: 86px; }
  .card--back .brand { left: 121px; top: 62px; }
  .card--back .brand__name { font-size: 28px; }
  .card--back .brand__tagline { font-size: 10.5px; margin-top: 1px; }

  .backdrop-shape { position: absolute; left: 0; top: 0; width: 513px; height: 284px; }
  .backdrop-shape circle { fill: var(--card-navy-deep); }

  .contact { position: absolute; left: 43px; top: 160px; }
  .contact__name { font-size: 19px; font-weight: 400; line-height: 22px; }
  .contact__role { font-size: 12px; line-height: 14px; margin-top: 2px; }
  .contact__list { list-style: none; margin-top: 18px; }
  .contact__item {
    display: flex; align-items: center; gap: 5px;
    font-size: 13px; line-height: 16px; color: var(--ink-soft); white-space: nowrap;
  }
  .contact__item svg { width: 10px; height: 10px; fill: var(--ink-white); flex: none; }
</style>
</head>
<body>
<main class="canvas">
  <section class="card card--front" aria-label="Card front">
    <span class="brand-mark" aria-hidden="true"></span>
    <div class="brand">
      <span class="brand__name">CRESTLINE</span>
      <span class="brand__tagline">Orthopaedic &amp; Sports<br>Medicine Center</span>
    </div>
  </section>

  <section class="card card--back" aria-label="Card back">
    <svg class="backdrop-shape" viewBox="0 0 513 284" aria-hidden="true">
      <circle cx="420" cy="175" r="150"/>
    </svg>

    <span class="brand-mark" aria-hidden="true"></span>
    <div class="brand">
      <span class="brand__name">CRESTLINE</span>
      <span class="brand__tagline">Orthopaedic &amp; Sports<br>Medicine Center</span>
    </div>

    <div class="contact">
      <p class="contact__name">Warren Ashby</p>
      <p class="contact__role">CEO</p>
      <ul class="contact__list">
        <li class="contact__item">
          <svg viewBox="0 0 10 10" aria-hidden="true"><path d="M5 0a3.5 3.5 0 0 0-3.5 3.5C1.5 6 5 10 5 10s3.5-4 3.5-6.5A3.5 3.5 0 0 0 5 0zm0 5a1.4 1.4 0 1 1 0-2.8A1.4 1.4 0 0 1 5 5z"/></svg>
          1820 Harlow Ave., Fairbrook, LA 70999
        </li>
        <li class="contact__item">
          <svg viewBox="0 0 10 10" aria-hidden="true"><path d="M2 0.5l1.6 2.2-1 1a6 6 0 0 0 3.7 3.7l1-1L9.5 8 8.3 9.5C4 9.3 0.7 6 0.5 1.7z"/></svg>
          (555) 014-2290
        </li>
        <li class="contact__item">
          <svg viewBox="0 0 10 10" aria-hidden="true"><path d="M0 2h10v6H0z M0 2l5 3.5L10 2" stroke="#0c2b5f" stroke-width="0.8"/></svg>
          washby@crestlineortho.com
        </li>
      </ul>
    </div>
  </section>
</main>
</body>
</html>
```